PSD web site UI

I need a PSD of a web site interface that I can use to build a theme with, which will be used on www.plovix.com, an up-and-coming CMS platform that I developed.

Follow the specifications included within the RAR file download below, and use the included PSD as a reference to make your own unique UI design.

Winners will be chosen based on how clean & professional the design looks, by how many unique panel designs are included within the UI, and by how large of a target market could actually use the design for their business web site.

Contest winners will only need to provide their PSD as completed work.

Download the PSD mockup at the bottom of this page to get started right away!
Updates

Project Deadline Extended
Reason: It was requested that I extend the deadline

Target Market(s)

small businesses and freelance designers, photographers & artists.

Industry/Entity Type

Business

Requirements
Must have
• Your PSD can have any color scheme you want. It can be light, dark, green, blue, multi-colored, paper, metallic, glossy, shiny, solid, gradients, or any theme you can imagine. Be creative, but keep the design looking Web 2.0 & professional. The width of your design can be 960 pixels wide like in the provided mockup PSD, or it can be a 100% width design if you'd like.

-
Panels
-
Each theme requires a minimum of 5 panel designs, which is basically a box that can stretch to a specific width or that stretches to 100% width of the web site. These 5 panels include a header, body, footer, child (that is placed within the body panel), and an alternative body panel. Of course, you can create as many panels as you like to create a more custom theme. Your panels do not have to look like the ones provided in the PSD mockup. They don't have to be completely square with round corners. They could be a bubbly cloud, or wavy, or include garnish around the edges, or be torn paper, or anything you like. Also, you can include a title within some of your panels, which is basically a header design with text at the top of the panel.

Each panel must contain a set of elements that fit the design of the panel. The body of your design should also include this set of elements. These elements include at least one menu, a set of buttons, lorum ipsum text & an anchor link, and form elements, such as a textbox, dropdown, & checkbox.

-
body
-
The body of your design should use a texture, gradient, solid color, or a background image that stretches 100% width. If you separate the body of your design into sectioned rows, each row will be treated like a panel.

-
Dashboard section
-
After a user logs into their account on Plovix.com, they manage their web site via a dashboard. This dashboard has a complex design, but can be partially customized. All elements within the header of the dashboard can be rearranged. This includes the title, screenshot, section title, and section menu. The main menu on the left contains a list of sections within the dashboard, which when clicked, will load the section title & menu in the dashboard header, and load the section page within the body of the dashboard.

Dashboard Icons:
The main menu & other menus within the dashboard contain icons. You can create your own custom icon library to use with your theme if you'd like, and the toolkit comes with a complete set of icons to use if you choose not to create your own library.

Dashboard body:
Each row within the dashboard body (options, search, results, paging) can use a panel design, but the entire dashboard body can also use a panel design as well, so you could design your dashboard body to use just one encompassing panel instead of separate panels for each row if you wanted.

-
Buttons
-
Each panel must contain a set of buttons. Each button requires a regular design as well as a mouse-over design. These types of buttons include: default, apply, cancel, previous, next, and delete (delete should stay small like a "close window" button).

-
Menus
-
Each menu requires a mouse-over design & selected item design.
You can make many types of menus; vertical, horizontal, small, and large.
Each item in the menu can be uniquely designed to create a sequence of menu items. For example, grey, white, grey, white, etc..

-
Photo Gallery
-
each photo container can be uniquely designed, creating a sequence of designs in a list.

-
Comments
-
each comment post can be uniquely designed, creating a sequence of designs in a list.
This will be used for comments as well as twitter feeds.

-
Blog Entries
-
Create designs for a blog summary list & a blog entry details.

Each blog entry (summary or details) can be uniquely designed, creating a sequence of designs in a list.

You could display a title, date created, tag words, summary, and the entry text, but you don't have to display all fields.

-
Product List
-
Products can be displayed many different ways:

product details, list grid, list rows, or even featured products list (with a flashy design).

You can display the product title, price, sale price & sale end date, description, photo & photo gallery, add to cart button, and view product details button. You don't have to display all fields for each design. You could show just a photo & title with summary & no price, or just a photo & title, or just the photo if you wanted.

-
Form elements
-
The textbox can look completely custom, have rounded corners, a textured background, or look plain if you want. The other form elements on the other hand can only be manipulated by CSS, so are very limited in design. Only border color, background color, and text color can be changed. The drop down box can have a custom drop down arrow though.

-
Header Panel
-
Requires a horizontal menu system that can be used for the web site's main menu

-
Footer Panel
-
The footer should be 100% width. Many web sites these days have very creative footers.
Should not have
• Don't use the mockup to just make color changes. I want a completely custom design that uses the structure of the mockup, but has a unique theme to the design, such as paper, dark grungy, cartoonish, hand-drawn, etc. Impress me & impress yourself!

```html
<!DOCTYPE html>
<html lang="en">
<head>
<meta charset="utf-8">
<title>Plovix Theme UI</title>
<link href="https://fonts.googleapis.com/css2?family=Questrial&display=swap" rel="stylesheet">
<style>
:root{
  --ink:#1b1b1b;
  --text:#333;
  --muted:#8a8a8a;
  --line:#dcdcdc;
  --panel:#f7f7f7;
  --panel-hi:#ffffff;
  --dark:#2a2a2a;
  --darker:#111;
  --accent:#7d5aa6;
  --accent-deep:#4b2a75;
  --link:#d4c21a;
}
*{box-sizing:border-box;margin:0;padding:0}
html,body{width:1200px;height:2214px;overflow:hidden}
body{position:relative;background:#fff;font-family:"Questrial",sans-serif;color:var(--text);font-size:14px}
.abs{position:absolute}
.icon{width:22px;height:22px;fill:var(--ink);vertical-align:middle}
.btn{position:absolute;display:flex;align-items:center;justify-content:center;gap:8px;color:#fff;font-size:14px;
  background:linear-gradient(#3a3a3a,#0c0c0c);border:1px solid #000;border-radius:3px;box-shadow:0 1px 2px rgba(0,0,0,.35)}
.btn svg{width:14px;height:14px;fill:#fff}
.close{position:absolute;width:22px;height:22px;border-radius:50%;background:var(--ink);display:flex;align-items:center;justify-content:center}
.close svg{width:10px;height:10px;stroke:#fff;stroke-width:3}
.close.light{background:#fff}
.close.light svg{stroke:var(--ink)}
.panel{position:absolute;background:linear-gradient(var(--panel-hi),var(--panel));border:1px solid var(--line);border-radius:4px;box-shadow:0 1px 3px rgba(0,0,0,.08)}
.field{position:absolute;height:24px;border:1px solid #ddd;background:#fff;color:#7a6a9a;font-size:14px;padding:3px 10px;border-radius:2px}
.photo{position:absolute;border-radius:4px;border:2px solid #222;box-shadow:0 2px 4px rgba(0,0,0,.4)}

/* top header */
.site-header{position:absolute;left:0;top:0;width:1200px;height:92px;background:linear-gradient(#3b3b3b,#0a0a0a)}
.brand{position:absolute;font-size:36px;color:#fff;letter-spacing:1px}
.main-nav{position:absolute;left:598px;top:14px;display:flex;gap:30px}
.main-nav a{display:flex;flex-direction:column;align-items:center;gap:6px;color:#fff;font-size:15px;text-decoration:none}
.main-nav svg{width:32px;height:32px;fill:#fff}
.header-rule{position:absolute;left:0;top:97px;width:1200px;height:8px;background:#eee}

/* dashboard header */
.dash-head{position:absolute;left:0;top:115px;width:1200px;height:155px;background:linear-gradient(#f3f3f3,#fff);border-bottom:1px solid #e2e2e2}
.screenshot{left:207px;top:13px;width:194px;height:130px;border:2px solid #333;background:linear-gradient(#9a7f6e,#6e5c66 55%,#b49a7a)}
.site-title{left:481px;top:17px;font-size:26px;color:var(--ink)}
.section-title{left:860px;top:21px;font-size:26px;color:var(--ink)}
.create-entry{left:837px;top:100px;font-size:14px;color:#444;display:flex;gap:8px;align-items:center}

/* side menu */
.side-menu{left:199px;top:300px;width:145px;height:253px;padding:10px 6px}
.side-menu li{list-style:none;height:29px;display:flex;align-items:center;gap:12px;font-size:14px;color:#222;padding-left:4px}
.side-menu li.selected{background:#ececec;border:1px solid #ddd;border-radius:3px}

.tool{position:absolute;display:flex;align-items:center;gap:6px;font-size:14px;color:#333}
.tool svg{width:20px;height:20px;fill:var(--ink)}
.entry h3{position:absolute;left:34px;top:20px;font-size:21px;font-weight:400;color:var(--ink)}
.entry p{position:absolute;left:34px;top:50px;font-size:11px;color:var(--muted)}
.check{position:absolute;left:14px;top:24px;width:13px;height:13px;border:1px solid #999;background:#fff}
.check svg{width:11px;height:11px;stroke:#222;stroke-width:2;fill:none}

/* dark strip panel */
.strip{left:195px;top:738px;width:826px;height:108px;background:linear-gradient(#4a4a4a,#333);border-radius:4px;box-shadow:0 2px 4px rgba(0,0,0,.3)}
.mini-menu li{list-style:none;height:31px;display:flex;align-items:center;gap:10px;font-size:15px;padding-left:8px;width:135px}
.strip .mini-menu li{color:#fff}
.strip .mini-menu li.selected{background:#1f1f1f;border-radius:3px}
.strip-nav{position:absolute;left:452px;top:38px;display:flex;gap:44px;color:#ddd;font-size:16px}

/* comments */
.comment{background:#fff}
.comment .avatar{position:absolute;top:-2px;width:108px;height:84px;border:3px solid #222;background:linear-gradient(#c9a48a,#8d6d5a)}
.comment p{position:absolute;font-size:14px;color:#222;line-height:18px}
.comment small{position:absolute;font-size:14px;color:var(--accent)}

/* calendar */
.calendar{left:748px;top:1007px;width:235px;height:186px;background:#111;border:3px solid #3a3a3a;border-radius:4px;padding:4px}
.calendar table{width:100%;border-collapse:collapse;color:#eee;font-size:10px}
.calendar th{font-weight:400;color:#aaa;height:20px;background:#2a2a2a}
.calendar td{height:30px;border:1px solid #444;text-align:center;vertical-align:top;padding-top:3px}

/* blog */
.card{background:linear-gradient(#f7f7f7,#fff)}
.card h4{position:absolute;left:16px;top:14px;font-size:18px;font-weight:400;color:#444;line-height:21px}
.card p{position:absolute;left:16px;top:74px;width:140px;font-size:10px;color:#999;line-height:13px}
.article h2{font-size:27px;font-weight:400;color:var(--ink)}
.article .date{font-size:11px;color:#999;margin:8px 0 20px}
.article p{font-size:12px;line-height:17px;color:#444}

/* products */
.product-hero{left:201px;top:1767px;width:177px;height:181px;border:4px solid var(--accent-deep);border-radius:3px;background:linear-gradient(#e6e9ee,#c9ced6)}
.price-old{font-size:16px;color:#555}
.price-new{font-size:27px;color:var(--accent-deep)}
.thumb{border:4px solid #222;border-radius:4px;background:linear-gradient(#cfd6df,#8b99aa)}
.p-name{position:absolute;font-size:17px;color:#333}
.p-price{position:absolute;font-size:12px;color:var(--accent-deep)}

/* footer */
.site-footer{position:absolute;left:0;top:2022px;width:1200px;height:192px;background:linear-gradient(#333,#232323)}
.site-footer .mini-menu li{color:#fff}
.site-footer .mini-menu li.selected{background:#1a1a1a;border-radius:3px}
</style>
</head>
<body>
<svg width="0" height="0" style="position:absolute">
  <defs>
    <symbol id="i-pages" viewBox="0 0 20 20"><rect x="3" y="1" width="12" height="16"/><rect x="6" y="4" width="12" height="15" fill="#fff"/><rect x="6" y="4" width="12" height="15" fill="none" stroke="currentColor"/><path d="M8 8h8M8 11h8M8 14h8" stroke="#000" stroke-width="1.4"/></symbol>
    <symbol id="i-media" viewBox="0 0 20 20"><path d="M1 3h18v14H1z M3 5v10h14V5z" fill-rule="evenodd"/><path d="M4 14l4-5 3 3 2-2 3 4z"/></symbol>
    <symbol id="i-msg" viewBox="0 0 20 20"><path d="M10 3c5 0 9 2.7 9 6s-4 6-9 6c-1 0-2 0-3-.3L3 17l1-3.5C2 12.4 1 10.8 1 9c0-3.3 4-6 9-6z"/></symbol>
    <symbol id="i-chart" viewBox="0 0 20 20"><path d="M2 17h16v1H2zM3 11h2v6H3zM7 7h2v10H7zM11 9h2v8h-2zM15 4h2v13h-2z"/></symbol>
    <symbol id="i-map" viewBox="0 0 20 20"><path d="M1 4l6-2 6 2 6-2v14l-6 2-6-2-6 2zM7 4v12M13 6v12" stroke="#fff" stroke-width="1"/></symbol>
    <symbol id="i-gear" viewBox="0 0 20 20"><path d="M9 1h2l.5 2.5 2 .8 2-1.5 1.5 1.5-1.5 2 .8 2L19 9v2l-2.5.5-.8 2 1.5 2-1.5 1.5-2-1.5-2 .8L11 19H9l-.5-2.5-2-.8-2 1.5L3 15.7l1.5-2-.8-2L1 11V9l2.5-.5.8-2-1.5-2L4.3 3l2 1.5 2-.8z"/><circle cx="10" cy="10" r="3" fill="#fff"/></symbol>
    <symbol id="i-install" viewBox="0 0 20 20"><path d="M8 1h4v7h3l-5 5-5-5h3z"/><path d="M1 12h4l2 3h6l2-3h4v7H1z"/></symbol>
    <symbol id="i-feed" viewBox="0 0 20 20"><rect x="1" y="1" width="18" height="18" rx="2"/><circle cx="6" cy="14" r="1.6" fill="#fff"/><path d="M5 9a6 6 0 0 1 6 6M5 5a10 10 0 0 1 10 10" stroke="#fff" stroke-width="1.6" fill="none"/></symbol>
    <symbol id="i-edit" viewBox="0 0 32 32"><path d="M4 6h16v3H7v16h16V14h3v14H4z"/><path d="M14 18l12-12 3 3-12 12-4 1z"/></symbol>
    <symbol id="i-people" viewBox="0 0 32 32"><circle cx="10" cy="8" r="4"/><circle cx="22" cy="8" r="4"/><circle cx="16" cy="10" r="4.5"/><path d="M3 26v-8c0-3 3-5 7-5h12c4 0 7 2 7 5v8z"/></symbol>
    <symbol id="i-brush" viewBox="0 0 32 32"><path d="M28 2l2 2-14 16-4-4z"/><path d="M11 17l4 4c0 5-5 9-12 8 3-2 2-6 4-9 1-2 3-3 4-3z"/></symbol>
    <symbol id="i-mail" viewBox="0 0 32 32"><path d="M2 7h28v18H2z"/><path d="M3 8l13 10L29 8" stroke="#000" stroke-width="1.5" fill="none"/></symbol>
    <symbol id="i-plus" viewBox="0 0 20 20"><rect width="20" height="20" rx="2"/><path d="M10 4v12M4 10h12" stroke="#fff" stroke-width="3"/></symbol>
    <symbol id="i-folder" viewBox="0 0 20 20"><path d="M1 4h7l2 2h9v11H1z"/></symbol>
    <symbol id="i-select" viewBox="0 0 20 20"><path d="M2 2h12v12H2z"/><path d="M5 8l3 3 7-8" stroke="#fff" stroke-width="2" fill="none"/><path d="M16 6h2v12H6v-2h10z"/></symbol>
    <symbol id="i-move" viewBox="0 0 20 20"><path d="M1 6h7l2 2h9v10H1z"/><path d="M8 2h6v2h4l-7 5-7-5h4z" fill="#888"/></symbol>
    <symbol id="i-left" viewBox="0 0 14 14"><path d="M10 1L4 7l6 6" stroke="#fff" stroke-width="3" fill="none"/></symbol>
    <symbol id="i-right" viewBox="0 0 14 14"><path d="M4 1l6 6-6 6" stroke="#fff" stroke-width="3" fill="none"/></symbol>
    <symbol id="i-x" viewBox="0 0 10 10"><path d="M1 1l8 8M9 1l-8 8"/></symbol>
    <symbol id="i-cart" viewBox="0 0 40 30"><path d="M4 10h32l-4 16H8z" fill="none" stroke="#666" stroke-width="2"/><path d="M12 10l4-8M28 10l-4-8" stroke="#666" stroke-width="2"/></symbol>
  </defs>
</svg>

<!-- Site header -->
<header class="site-header">
  <div class="brand" style="left:211px;top:20px">PLOVIX</div>
  <nav class="main-nav">
    <a href="#"><svg><use href="#i-edit"/></svg>Dashboard</a>
    <a href="#"><svg><use href="#i-people"/></svg>Community</a>
    <a href="#"><svg><use href="#i-brush"/></svg>Developers</a>
    <a href="#"><svg><use href="#i-mail"/></svg>Support</a>
  </nav>
</header>
<div class="header-rule"></div>

<!-- Dashboard header -->
<section class="dash-head">
  <div class="abs screenshot" role="img" aria-label="Screenshot of the user's web site"></div>
  <div class="abs" style="left:418px;top:22px;display:flex;gap:4px">
    <svg class="icon" style="width:22px;height:22px"><use href="#i-media"/></svg>
    <svg class="icon" style="width:22px;height:22px"><use href="#i-chart"/></svg>
  </div>
  <div class="abs site-title">Dana Whitfield</div>
  <svg class="abs icon" style="left:819px;top:15px;width:34px;height:38px"><use href="#i-feed"/></svg>
  <div class="abs section-title">Blog Book</div>
  <div class="abs create-entry"><svg class="icon" style="width:18px;height:18px"><use href="#i-plus"/></svg>Create New Entry</div>
</section>

<!-- Dashboard side menu -->
<ul class="panel side-menu">
  <li><svg class="icon"><use href="#i-pages"/></svg>Pages</li>
  <li><svg class="icon"><use href="#i-media"/></svg>Media</li>
  <li><svg class="icon"><use href="#i-msg"/></svg>Messages</li>
  <li><svg class="icon"><use href="#i-chart"/></svg>Analytics</li>
  <li><svg class="icon"><use href="#i-map"/></svg>Site Map</li>
  <li><svg class="icon"><use href="#i-gear"/></svg>Settings</li>
  <li><svg class="icon"><use href="#i-install"/></svg>Install Apps</li>
  <li class="selected"><svg class="icon"><use href="#i-feed"/></svg>Blog Book</li>
</ul>

<!-- Dashboard options -->
<div class="panel" style="left:351px;top:300px;width:667px;height:116px">
  <div class="abs" style="left:24px;top:19px;font-size:14px">Folder</div>
  <div class="abs" style="left:77px;top:14px;width:232px;height:24px;border:1px solid #ccc;border-radius:3px;background:linear-gradient(#fff,#eee)">
    <svg class="abs" style="right:8px;top:8px;width:10px;height:8px"><path d="M0 0h10L5 7z" fill="#5a4a8a"/></svg>
  </div>
  <div class="tool" style="left:24px;top:78px"><svg><use href="#i-folder"/></svg>Create New Folder</div>
  <div class="tool" style="left:185px;top:78px"><svg><use href="#i-select"/></svg>Select All Entries</div>
  <div class="tool" style="left:337px;top:78px"><svg><use href="#i-move"/></svg>Move Selected Entries to Folder</div>
</div>

<!-- Dashboard search -->
<div class="panel" style="left:351px;top:424px;width:667px;height:53px">
  <div class="field" style="left:16px;top:12px;width:208px;font-size:11px;color:#aaa;background:#f4f4f4">search blog entries</div>
  <div class="btn" style="left:228px;top:12px;width:72px;height:24px;font-size:12px">Search</div>
</div>

<!-- Dashboard results -->
<div class="panel entry" style="left:351px;top:480px;width:667px;height:82px">
  <div class="check"><svg><path d="M1 5l3 3 6-7"/></svg></div>
  <h3>A day in the life of Owen Castell.</h3>
  <p>Explore how Owen Castell spends his time in the Plovix offices.</p>
  <div class="close" style="right:8px;top:10px"><svg><use href="#i-x"/></svg></div>
</div>
<div class="panel entry" style="left:351px;top:567px;width:667px;height:82px">
  <div class="check"><svg><path d="M1 5l3 3 6-7"/></svg></div>
  <h3>A day in the life of Owen Castell.</h3>
  <p>Explore how Owen Castell spends his time in the Plovix offices.</p>
  <div class="close" style="right:8px;top:10px"><svg><use href="#i-x"/></svg></div>
</div>

<!-- Dashboard paging -->
<div class="panel" style="left:351px;top:657px;width:667px;height:51px">
  <div class="btn" style="left:405px;top:10px;width:125px;height:30px;font-size:16px"><svg><use href="#i-left"/></svg>PREVIEW</div>
  <div class="btn" style="left:549px;top:10px;width:104px;height:30px;font-size:16px">MORE<svg><use href="#i-right"/></svg></div>
</div>

<!-- Dark body panel -->
<div class="abs strip">
  <ul class="mini-menu abs" style="left:7px;top:6px">
    <li class="selected"><svg class="icon" style="fill:#fff"><use href="#i-pages"/></svg>Pages</li>
    <li style="background:#2a2a2a;border-radius:3px"><svg class="icon" style="fill:#fff"><use href="#i-media"/></svg>Media</li>
    <li><svg class="icon" style="fill:#fff"><use href="#i-msg"/></svg>Messages</li>
  </ul>
  <div class="btn" style="left:152px;top:6px;width:103px;height:26px;font-size:13px">Browse</div>
  <div class="btn" style="left:152px;top:38px;width:103px;height:26px;font-size:13px;background:linear-gradient(#2c2c2c,#141414)">Apply</div>
  <div class="close light" style="left:261px;top:6px"><svg><use href="#i-x"/></svg></div>
  <div class="abs" style="left:158px;top:74px;font-size:13px;color:#fff">Lorem ipsum dolor sit amet <a href="#" style="color:var(--link);margin-left:8px">Click here</a></div>
  <nav class="strip-nav"><span>Projects</span><span>Team</span><span>Mantra</span><span>Contact</span></nav>
  <svg class="abs" style="left:610px;top:62px;width:40px;height:30px;opacity:.5"><use href="#i-cart"/></svg>
</div>

<!-- Photo gallery -->
<div class="photo" style="left:195px;top:872px;width:148px;height:107px;background:linear-gradient(135deg,#2c2c30,#8a8c95 50%,#25252a)" role="img" aria-label="Fantasy art portrait in cool grey tones"></div>
<div class="photo" style="left:351px;top:872px;width:140px;height:107px;background:linear-gradient(135deg,#3a2a22,#a07d66 50%,#3b2219)" role="img" aria-label="Fantasy art portrait in warm sepia tones"></div>
<div class="photo" style="left:506px;top:872px;width:148px;height:107px;background:radial-gradient(circle,#7a746e,#2a2725 70%)" role="img" aria-label="Fantasy art portrait in dark muted tones"></div>

<!-- Alternative menu -->
<ul class="mini-menu abs" style="left:676px;top:872px">
  <li style="background:linear-gradient(#3a3a3a,#111);color:#fff;border-radius:3px"><svg class="icon" style="fill:#fff"><use href="#i-pages"/></svg>Pages</li>
  <li style="color:var(--accent)"><svg class="icon"><use href="#i-media"/></svg>Media</li>
  <li style="color:var(--accent)"><svg class="icon"><use href="#i-msg"/></svg>Messages</li>
</ul>
<div class="btn" style="left:820px;top:872px;width:103px;height:28px;font-size:13px">Browse</div>
<div class="btn" style="left:820px;top:904px;width:103px;height:28px;font-size:13px">Apply</div>
<div class="close" style="left:929px;top:875px"><svg><use href="#i-x"/></svg></div>
<div class="abs" style="left:828px;top:940px;font-size:14px;color:#444">Check Here</div>

<!-- Comments -->
<div class="panel comment" style="left:202px;top:1011px;width:473px;height:81px">
  <div class="avatar" style="left:0" role="img" aria-label="Commenter portrait photo"></div>
  <svg class="abs" style="left:108px;top:24px;width:10px;height:18px"><path d="M0 0l10 9-10 9z" fill="#222"/></svg>
  <p style="left:133px;top:10px;width:330px">Owen says, “This is quite incredible. I can build an entire web site without even using my brain.”</p>
  <small style="left:133px;top:54px">Posted 47 minutes ago</small>
</div>
<div class="panel comment" style="left:202px;top:1114px;width:473px;height:79px">
  <div class="avatar" style="left:365px;background:linear-gradient(#6e5548,#3a2d28)" role="img" aria-label="Commenter portrait photo"></div>
  <svg class="abs" style="left:355px;top:24px;width:10px;height:18px"><path d="M10 0L0 9l10 9z" fill="#222"/></svg>
  <p style="left:20px;top:10px;width:330px">Marta says, “Make a web site for me, Owen! I’ve always wanted to showcase my artwork.”</p>
  <small style="left:20px;top:54px">Posted 22 minutes ago</small>
</div>

<!-- Calendar -->
<div class="abs calendar">
  <table>
    <tr><th>Sun</th><th>Mon</th><th>Tue</th><th>Wed</th><th>Thur</th><th>Fri</th><th>Sat</th></tr>
    <tr><td></td><td></td><td></td><td>1</td><td>2</td><td>3</td><td>4</td></tr>
    <tr><td>5</td><td>6</td><td>7</td><td>8</td><td>9</td><td>10</td><td>11</td></tr>
    <tr><td>12</td><td>13</td><td>14</td><td>15</td><td>16</td><td>17</td><td>18</td></tr>
    <tr><td>5</td><td>6</td><td>7</td><td>8</td><td>9</td><td>10</td><td>11</td></tr>
    <tr><td>26</td><td>27</td><td>28</td><td>29</td><td>30</td><td></td><td></td></tr>
  </table>
</div>

<!-- Comment bar -->
<div class="panel" style="left:202px;top:1218px;width:473px;height:40px;background:#fff">
  <div class="btn" style="left:8px;top:6px;width:160px;height:27px;font-size:14px">Leave a comment</div>
  <div class="btn" style="left:372px;top:6px;width:92px;height:27px;font-size:14px">More<svg style="margin-left:14px"><use href="#i-right"/></svg></div>
</div>

<!-- Comment form -->
<form class="panel" style="left:202px;top:1274px;width:473px;height:224px;background:#fff">
  <div class="abs" style="left:16px;top:12px;font-size:14px;color:#333">Leave a comment</div>
  <div class="field" style="left:16px;top:38px;width:162px;background:#f6f4f8">your name</div>
  <div class="field" style="left:278px;top:38px;width:162px;background:#f6f4f8">web site (optional)</div>
  <div class="field" style="left:16px;top:74px;width:162px;background:#f6f4f8">your email</div>
  <div class="abs" style="left:16px;top:116px;width:429px;height:60px;border:2px solid #e2e2e2;border-radius:2px"></div>
  <div class="btn" style="left:282px;top:186px;width:163px;height:27px;font-size:14px">submit comment</div>
</form>

<!-- Blog summaries -->
<div class="panel card" style="left:202px;top:1525px;width:171px;height:195px">
  <h4>Spending money<br>the right way.</h4>
  <p>Why is it that we buy things that we don’t need at all? I’ll share my secrets with you on how to make money by spending money!</p>
  <div class="btn" style="left:44px;top:154px;width:77px;height:28px;font-size:14px">Read...</div>
</div>
<div class="panel card" style="left:381px;top:1525px;width:172px;height:195px">
  <h4>Build a startup,<br>not a resume.</h4>
  <p>If you want to succeed, build a startup or be a part of one. If you want to be stagnant, find a day job. Startup = win.</p>
  <div class="btn" style="left:46px;top:154px;width:77px;height:28px;font-size:14px">Read...</div>
</div>

<!-- Blog detail -->
<article class="abs article" style="left:583px;top:1521px;width:400px">
  <h2>Build a startup, not a resume.</h2>
  <div class="date">Published Friday, September 13th.</div>
  <p>Lorem ipsum dolor sit amet, consectetur adipiscing elit. In eget mauris velit, at ultricies risus. Nam vel consectetur tortor. Duis non iaculis massa. Maecenas ac eros arcu, nec facilisis mi. Nam iaculis dapibus ligula, ac laoreet nunc blandit vitae. Curabitur eget tellus leo, pretium aliquam enim. Aenean orci ligula, iaculis nec porta nec, sollicitudin ut neque. Duis sit amet urna id...</p>
</article>

<!-- Featured product -->
<div class="abs product-hero" role="img" aria-label="Hand holding a tablet showing its home screen"></div>
<div class="abs" style="left:404px;top:1770px;font-size:27px;color:var(--ink)">Slate mini</div>
<div class="abs" style="left:404px;top:1808px;display:flex;align-items:baseline;gap:8px">
  <span class="price-old">was <s>$599<sup style="font-size:9px">00</sup></s></span>
  <span class="price-old">now</span>
  <span class="price-new">$429<sup style="font-size:14px;text-decoration:underline">00</sup></span>
</div>
<p class="abs" style="left:396px;top:1852px;width:220px;font-size:14px;line-height:16px;color:#444">Everything you love about Slate... the beautiful screen, fast and fluid performance, 10-hour battery life...</p>
<div class="btn" style="left:511px;top:1917px;width:97px;height:30px;font-size:14px">Buy Now</div>

<!-- Product grid -->
<div class="abs thumb" style="left:654px;top:1767px;width:118px;height:118px" role="img" aria-label="Tablet product photo"></div>
<div class="abs thumb" style="left:778px;top:1767px;width:116px;height:118px" role="img" aria-label="Phone product photo"></div>
<div class="abs thumb" style="left:902px;top:1767px;width:116px;height:118px" role="img" aria-label="Music player product photo"></div>
<div class="p-name" style="left:656px;top:1890px">Slate Mini</div>
<div class="p-price" style="left:656px;top:1914px">$429<sup style="font-size:7px">00</sup></div>
<div class="p-name" style="left:779px;top:1890px">Nova Phone 5</div>
<div class="p-price" style="left:779px;top:1914px">$359<sup style="font-size:7px">00</sup></div>
<div class="p-name" style="left:904px;top:1890px">Tune Nano</div>
<div class="p-price" style="left:904px;top:1914px">$89<sup style="font-size:7px">00</sup></div>

<!-- Footer -->
<footer class="site-footer">
  <div class="brand" style="left:211px;top:38px">PLOVIX</div>
  <div class="abs" style="left:211px;top:90px;font-size:13px;color:#fff">Lorem ipsum dolor sit amet.</div>
  <a class="abs" href="#" style="left:211px;top:114px;font-size:14px;color:#fff">Click here</a>
  <ul class="mini-menu abs" style="left:400px;top:38px">
    <li class="selected"><svg class="icon" style="fill:#fff"><use href="#i-pages"/></svg>Pages</li>
    <li style="background:#2b2b2b;border-radius:3px"><svg class="icon" style="fill:#fff"><use href="#i-media"/></svg>Media</li>
    <li><svg class="icon" style="fill:#fff"><use href="#i-msg"/></svg>Messages</li>
  </ul>
  <div class="btn" style="left:543px;top:40px;width:103px;height:27px;font-size:13px">Browse</div>
  <div class="btn" style="left:543px;top:72px;width:103px;height:27px;font-size:13px">Apply</div>
  <div class="close light" style="left:652px;top:42px"><svg><use href="#i-x"/></svg></div>
  <div class="abs" style="left:550px;top:110px;font-size:13px;color:#fff">Lorem ipsum dolor sit amet</div>
</footer>
</body>
</html>
```